Website Redesign for Pet Services Facility

We are looking to redesign our current website. The website must be designed in Wix so we can go in and easily edit throughout the life of the website. Design must be professional, simplistic and informative.

Our current website can be found at: www.pawlanelodge.com

I would like the new site to be on one scrolling page. Sections to include:
Home page
Service teaser: Overnight Care, Grooming, Dog Daycare, Retail
An about us area with text on the left and a video on the right
Testimonial section
Overnight Section
Grooming Section
Dog Daycare Section
Retail
Meet the Team
Contact us: address, phone number, hours, etc.
Newsletter sign up and location map

A second page will be used for reservations and should include fields for.
Name, address, phone number, service: Overnight care, grooming, daycare, Arrival date, departure date, pet name, breed, special requests

Our phone number should be easily found through the pages. 'Request a Reservation' buttons should be found throughout page.

Text from our current site can be uesd as a filler for now as I will go in and finalize text when site is complete. Any photos can be used for now as I will go in and choose final photos as a later date.

I started playing with wix and started with a concept that I can share if you are interested, just let me know.

Industry/Entity Type

Pet

Number of Pages Required

2 page

Font styles to use
Sans Serif

Requirements
Must have
• 'Request a Reservation' Buttons
• Phone number easily visible
• location map
• Hours area
• Newsletter sign up

```html
<!DOCTYPE html>
<html lang="en">
<head>
<meta charset="utf-8">
<title>Paw Lane Lodge</title>
<link href="https://fonts.googleapis.com/css2?family=Montserrat:ital,wght@0,400;0,500;0,600;0,700;1,400;1,500&display=swap" rel="stylesheet">
<style>
:root{
  --ink:#1c2b33;
  --sky:#aadde3;
  --lime:#a5c42c;
  --cornflower:#6699e0;
  --tab:#6a9ae2;
  --tab-open:#8db5f5;
  --panel:#aadde3;
  --red:#cc1a1a;
  --red-dark:#a81212;
  --player:#2b2b2b;
  --white:#ffffff;
}
*{box-sizing:border-box;margin:0;padding:0}
html,body{width:1200px;height:1200px;overflow:hidden;background:var(--white);font-family:"Montserrat",sans-serif;color:var(--ink)}
.page{position:relative;width:1200px;height:1200px;overflow:hidden}

.site-header{position:absolute;left:0;top:0;width:1200px;height:106px;background:var(--white)}
.brand{position:absolute;left:161px;top:15px;display:flex;align-items:flex-end;gap:15px}
.brand-mark{width:81px;height:74px;background:var(--sky)}
.brand-name{font-size:21px;font-weight:400;color:var(--ink);line-height:1;margin-bottom:-2px}
.phone{position:absolute;right:161px;top:28px;font-size:29px;font-weight:700;letter-spacing:-.3px;color:var(--ink)}
.main-nav{position:absolute;right:161px;top:76px;display:flex;gap:25px;font-size:14px;font-weight:600}

.hero-band{position:absolute;left:0;top:106px;width:1200px;height:330px;background:var(--sky)}
.hero{position:absolute;left:161px;top:16px;width:878px;height:300px;border-radius:4px;overflow:hidden;
  background:linear-gradient(180deg,#6f6f6f 0%,#3a3a3a 45%,#5a5a5a 80%,#8c8c8c 100%)}
.hero-strip{position:absolute;left:0;top:146px;width:100%;height:110px;background:rgba(40,40,40,.55)}
.hero-title{position:absolute;left:0;top:160px;width:100%;text-align:center;font-size:27px;font-weight:500;color:var(--white);text-shadow:0 1px 3px rgba(0,0,0,.6)}
.btn-reserve{position:absolute;width:224px;height:44px;border-radius:4px;background:var(--red);box-shadow:0 2px 0 var(--red-dark);
  color:var(--white);font-size:13px;font-weight:500;display:flex;align-items:center;justify-content:center;letter-spacing:.1px}
.hero .btn-reserve{left:327px;top:196px}
.dots{position:absolute;left:400px;top:270px;display:flex;gap:8px}
.dots span{width:13px;height:13px;border-radius:50%;border:2px solid var(--white);background:rgba(255,255,255,.25)}
.dots span.is-active{background:var(--lime)}

.about-band{position:absolute;left:0;top:451px;width:1200px;height:355px;background:var(--lime)}
.accordion{position:absolute;left:161px;top:16px;width:431px}
.acc-tab{height:51px;border-radius:4px;background:var(--tab);color:var(--white);font-size:22px;font-weight:400;
  display:flex;align-items:center;justify-content:center;text-shadow:0 1px 2px rgba(0,0,0,.35);margin-bottom:2px;box-shadow:0 2px 2px rgba(0,0,0,.15)}
.acc-tab.is-open{background:var(--tab-open);border-radius:4px 4px 0 0;height:50px;margin-bottom:0;border-bottom:2px solid #5b82c0}
.acc-panel{background:var(--panel);height:167px;padding:7px 33px 0;font-size:10.6px;font-style:italic;font-weight:500;line-height:12.6px;margin-bottom:3px;border-radius:0 0 4px 4px}
.acc-panel p{margin-bottom:13px}
.player{position:absolute;left:608px;top:16px;width:431px;height:324px;background:var(--player)}
.player-top{height:25px;color:#ccc;font-size:7px;padding:10px 0 0 12px;border-bottom:1px solid #444}
.player-video{position:absolute;left:1px;top:25px;width:429px;height:269px;background:linear-gradient(180deg,#5d7a57 0%,#6b9a4a 30%,#6fa648 65%,#5c8c3c 100%)}
.player-bar{position:absolute;left:0;bottom:0;width:100%;height:30px;display:flex;align-items:center;gap:9px;padding:0 10px;color:#ccc;font-size:7px}
.play{width:30px;height:20px;background:#444;display:flex;align-items:center;justify-content:center}
.track{flex:1;height:5px;border-radius:3px;background:#777;position:relative}
.track i{position:absolute;left:0;top:0;height:5px;width:75%;border-radius:3px;background:#2f7be0}

.opinion-band{position:absolute;left:0;top:821px;width:1200px;height:379px;background:var(--cornflower)}
.opinion-title{position:absolute;left:0;top:12px;width:1200px;text-align:center;font-size:21px;font-weight:700;color:var(--ink);padding-right:25px}
.avatar{position:absolute;width:157px;height:157px;border-radius:50%;border:3px solid var(--white);background:linear-gradient(160deg,#3a2a2a,#a87a62 60%,#e0b89a)}
.avatar.a1{left:163px;top:51px}
.avatar.a2{left:880px;top:253px;background:linear-gradient(160deg,#d8d0c8,#b07850 55%,#e6c2a6)}
.client-name{position:absolute;left:161px;top:222px;width:162px;text-align:center;font-size:14px;font-weight:700}
.quote{position:absolute;font-size:11.8px;font-style:italic;line-height:15.7px;color:var(--ink)}
.quote.q1{left:384px;top:107px;width:660px}
.quote.q2{left:161px;top:302px;width:660px}
.opinion-band .btn-reserve{left:489px;top:219px}
</style>
</head>
<body>
<div class="page">
  <header class="site-header">
    <div class="brand"><div class="brand-mark"></div><div class="brand-name">Paw Lane Lodge</div></div>
    <div class="phone">920-555-0147</div>
    <nav class="main-nav"><span>About Us</span><span>Client Stories</span><span>Services</span><span>Shop</span><span>Our Team</span><span>Contact Us</span></nav>
  </header>

  <section class="hero-band">
    <div class="hero" role="img" aria-label="Close-up photo of a dog's nose peeking over a wooden fence">
      <div class="hero-strip"></div>
      <h1 class="hero-title">Let’s Go to Paw Lane Lodge… Please!</h1>
      <div class="btn-reserve">REQUEST A RESERVATION</div>
      <div class="dots"><span class="is-active"></span><span></span><span></span><span></span></div>
    </div>
  </section>

  <section class="about-band">
    <div class="accordion">
      <div class="acc-tab">Our History</div>
      <div class="acc-tab is-open">Our Philosophy</div>
      <div class="acc-panel">
        <p>We are dedicated to the health and happiness or your pets.</p>
        <p>At Paw Lane Lodge we take pride in offering a wide variety of services, packages, high-quality retail goods, and a la carte offerings. Our philosophy behind this is simple: Every dog is unique. Not every dog wants to or is able to participate in daycare, not every dog is fed the same diet, and not every Golden Retriever is groomed the same way.</p>
        <p>A stay at Paw Lane Lodge, whether for the day or a weekend, is an experience unlike any other. From the moment you walk in the door it is easy to see that we have nothing but the best in store for you and your dog.</p>
      </div>
      <div class="acc-tab">Our Facility</div>
    </div>
    <div class="player">
      <div class="player-top">‹ &nbsp;Menu</div>
      <div class="player-video" role="img" aria-label="Video of dogs playing in a grassy yard with a staff member"></div>
      <div class="player-bar">
        <div class="play"><svg width="8" height="9" viewBox="0 0 8 9"><path d="M0 0L8 4.5L0 9Z" fill="#ccc"/></svg></div>
        <span>00:00</span><div class="track"><i></i></div><span>01:25</span>
        <svg width="10" height="9" viewBox="0 0 10 9"><path d="M0 3h2l3-3v9L2 6H0z" fill="#ccc"/></svg>
        <span style="margin-left:auto">›</span>
      </div>
    </div>
  </section>

  <section class="opinion-band">
    <h2 class="opinion-title">Client Opinion</h2>
    <div class="avatar a1" role="img" aria-label="Portrait photo of a client"></div>
    <div class="client-name">Mara Lindqvist</div>
    <p class="quote q1">Lorem ipsum dolor sit amet, consectetur adipiscing elit. Vestibulum a blandit urna. Ut eget sodales dui, eget iaculis arcu. In porta ullamcorper mauris, quis gravida dolor egestas ut. Morbi nec magna enim. Morbi sodales auctor feugiat. Pellentesque imperdiet ligula non sollicitudin blandit. In rutrum neque eget vulputate volutpat. Curabitur metus ligula, cursus ut dolor id, molestie mattis sem. Fusce mollis orci at augue dignissim tincidunt quis faucibus urna.</p>
    <div class="btn-reserve">REQUEST A RESERVATION</div>
    <p class="quote q2">Vestibulum cursus eu sem id dictum. Quisque quis condimentum eros, eu fringilla erat. Cras nec magna non quam consectetur consectetur. Morbi congue ligula lorem. Mauris ultrices volutpat orci, id varius magna pretium ac. Aliquam viverra nibh dolor, id cursus purus porttitor a. Praesent et hendrerit arcu. Ut molestie, massa vel convallis feugiat, erat sapien commodo nisi, non aliquet dolor elit eu velit. Integer id semper metus, sed ornare nisi. Suspendisse dictum malesuada sollicitudin.</p>
    <div class="avatar a2" role="img" aria-label="Portrait photo of a client"></div>
  </section>
</div>
</body>
</html>
```